We need business cards for Tarnwick Consulting. We have a logo that was recently designed. I would obviously like the logo on the card and to stay with similar fonts and colors.

I think the font is Trebuchet MS or something very close to it.
CMYK for the blue is C:100 M:100 Y:0 K:0
And for the green C:40 M:0 Y:40 K:0

Tarnwick Consulting is based in Wellington, New Zealand. Doing consulting and advisory work in Australia, PNG and NZ to government and private organisations.
We provide management guidance and consultancy on petroleum, gas and mineral (predominantly gold) projects. (Geophysical consulting).
We advise on design, contractor selection, tendering, risk assessment through to full project delivery and operational management

We are looking for a professional, corporate looking cards.

Industry/Entity Type

Business

```html
<!DOCTYPE html>
<html lang="en">
<head>
<meta charset="utf-8">
<title>Tarnwick Consulting – Business Cards</title>
<link rel="stylesheet" href="https://fonts.googleapis.com/css2?family=PT+Sans:wght@400;700&display=swap">
<style>
  :root {
    --brand-blue: #2f2a78;
    --brand-green: #93b31c;
    --card-white: #e9e9ea;
    --ink: #2b2b2b;
    --page: #f2f2f0;
  }
  * { box-sizing: border-box; margin: 0; padding: 0; }
  html, body {
    width: 1200px; height: 900px; overflow: hidden;
    background: var(--page);
    font-family: "PT Sans", "Trebuchet MS", sans-serif;
  }
  .sheet {
    width: 1200px; height: 900px;
    display: flex; align-items: center; justify-content: center; gap: 60px;
  }
  .card {
    position: relative;
    width: 520px; height: 297px;
    overflow: hidden;
    box-shadow: 0 2px 10px rgba(0,0,0,.12);
  }

  /* Front */
  .card--front { background: var(--brand-blue); }
  .front-brand {
    position: absolute; left: 70px; top: 122px;
    display: flex; align-items: center;
  }
  .brand-dot {
    width: 30px; height: 30px; border-radius: 50%;
    background: var(--brand-green);
  }
  .front-divider {
    width: 1px; height: 52px; background: var(--brand-green);
    margin: 0 18px 0 26px;
  }
  .front-name {
    color: #fff; font-size: 30px; font-weight: 400; letter-spacing: .5px;
  }

  /* Back */
  .card--back { background: var(--card-white); color: var(--ink); }
  .back-band {
    position: absolute; left: 0; right: 0; bottom: 0; height: 15px;
    background: var(--brand-blue);
  }
  .back-brand {
    position: absolute; left: 28px; top: 150px;
    color: var(--brand-blue); font-size: 17px; font-weight: 700;
  }
  .back-divider {
    position: absolute; left: 208px; top: 42px;
    width: 1px; height: 168px; background: var(--brand-green);
  }
  .details {
    position: absolute; left: 232px; top: 34px;
    font-size: 12px; line-height: 1.35;
  }
  .person-name { font-size: 18px; letter-spacing: .4px; line-height: 1.1; }
  .person-role { font-size: 13px; margin-bottom: 14px; }
  .contact-list { list-style: none; margin-bottom: 14px; }
  .contact-label { color: var(--brand-blue); display: inline-block; width: 12px; }
  .address { margin-bottom: 14px; }
  .website { color: var(--brand-blue); font-size: 13px; }
</style>
</head>
<body>
<main class="sheet">
  <section class="card card--front" aria-label="Card front">
    <div class="front-brand">
      <span class="brand-dot" aria-hidden="true"></span>
      <span class="front-divider" aria-hidden="true"></span>
      <span class="front-name">Tarnwick Consulting</span>
    </div>
  </section>

  <section class="card card--back" aria-label="Card back">
    <div class="back-brand">Tarnwick Consulting</div>
    <div class="back-divider" aria-hidden="true"></div>
    <div class="details">
      <h1 class="person-name">MAREN HOLLOWAY</h1>
      <p class="person-role">Director</p>
      <ul class="contact-list">
        <li><span class="contact-label">t</span> +64 4 5128037</li>
        <li><span class="contact-label">m</span> +64 21 430915</li>
        <li><span class="contact-label">e</span> maren@tarnwickconsulting.co.nz</li>
      </ul>
      <p class="address">14 Kowhai Rise, Ngaio 6035<br>Wellington, New Zealand</p>
      <p class="website">www.tarnwickconsulting.co.nz</p>
    </div>
    <div class="back-band" aria-hidden="true"></div>
  </section>
</main>
</body>
</html>
```